BRIM Outreach Partners Business Card Rebrand

Hello Designers! We are looking for help designing our new business card to go in conjunction with our company rebrand. Unfortunately, we have an event mid June that requires we get these printed ASAP (before our new website is launched.) We have a mostly complete Brand Book which I have uploaded to this request for your reference to company information, style, fonts. I've also enclosed our logo file in .eps & .jpg. Attached is a sample business card my boss liked but said was "too simple." I made it in Canva and do not profess to be a designer. NOT FOR DESIGN REFERENCE, ONLY FOR CONTEXT Here is what our old website looks like: https://brimoutreachpartners.com/.

```html
<!DOCTYPE html>
<html lang="en">
<head>
<meta charset="UTF-8">
<title>BRIM Outreach Partners – Business Card</title>
<link href="https://fonts.googleapis.com/css2?family=Nunito:wght@400;600;800&family=Nunito+Sans:wght@400;600&display=swap" rel="stylesheet">
<style>
  :root {
    --stage: #999999;
    --charcoal: #242424;
    --charcoal-soft: #373737;
    --paper: #ffffff;
    --brand-blue: #29b8fb;
    --ink: #1c1c1c;
    --muted: #7a7a7a;
    --light-text: #ececec;
  }
  * { box-sizing: border-box; margin: 0; padding: 0; }
  html, body {
    width: 1200px;
    height: 1200px;
    overflow: hidden;
    background: var(--stage);
  }
  .card {
    position: absolute;
    top: 226px;
    width: 436px;
    height: 746px;
    border-radius: 26px;
    overflow: hidden;
  }
  .card--front { left: 140px; background: var(--charcoal); }
  .card--back { left: 626px; background: var(--paper); }

  .card__arc {
    position: absolute;
    left: 0; top: 0;
    width: 436px; height: 746px;
  }

  .wordmark {
    position: absolute;
    display: flex;
    align-items: center;
    gap: 14px;
    font-family: "Nunito", sans-serif;
    font-weight: 800;
    line-height: 1.02;
  }
  .wordmark__dot {
    flex: none;
    border-radius: 50%;
    background: var(--brand-blue);
  }
  .card--front .wordmark {
    left: 54px; top: 168px;
    color: var(--light-text);
    font-size: 34px;
  }
  .card--front .wordmark__dot { width: 88px; height: 88px; }

  .card--back .wordmark {
    left: 0; right: 0; top: 60px;
    justify-content: center;
    color: var(--ink);
    font-size: 24px;
    gap: 12px;
  }
  .card--back .wordmark__dot { width: 58px; height: 58px; }

  .contact {
    position: absolute;
    left: 0; right: 0; top: 158px;
    text-align: center;
  }
  .contact__name {
    font-family: "Nunito", sans-serif;
    font-weight: 800;
    font-size: 29px;
    color: var(--brand-blue);
  }
  .contact__role {
    margin-top: 4px;
    font-family: "Nunito Sans", sans-serif;
    font-weight: 400;
    font-size: 14px;
    letter-spacing: 3.2px;
    color: var(--muted);
  }
  .contact__icons {
    margin-top: 28px;
    display: flex;
    justify-content: center;
    gap: 6px;
  }
  .contact__icon {
    width: 31px; height: 31px;
    border-radius: 50%;
    background: var(--brand-blue);
    display: flex; align-items: center; justify-content: center;
  }
  .contact__lines {
    margin-top: 14px;
    list-style: none;
    font-family: "Nunito Sans", sans-serif;
    font-size: 17px;
    line-height: 22px;
    color: var(--ink);
  }
</style>
</head>
<body>

<section class="card card--front" aria-label="Card front">
  <svg class="card__arc" viewBox="0 0 436 746" aria-hidden="true">
    <circle cx="219" cy="674" r="288" fill="var(--charcoal-soft)"/>
  </svg>
  <div class="wordmark">
    <span class="wordmark__dot"></span>
    <span class="wordmark__name">BRIM Outreach<br>Partners</span>
  </div>
</section>

<section class="card card--back" aria-label="Card back">
  <svg class="card__arc" viewBox="0 0 436 746" aria-hidden="true">
    <circle cx="219" cy="674" r="288" fill="var(--brand-blue)"/>
  </svg>
  <div class="wordmark">
    <span class="wordmark__dot"></span>
    <span class="wordmark__name">BRIM Outreach<br>Partners</span>
  </div>

  <div class="contact">
    <h1 class="contact__name">Martin Hale-Dorsey</h1>
    <p class="contact__role">MANAGING PARTNER</p>
    <div class="contact__icons">
      <span class="contact__icon" aria-label="Email">
        <svg width="17" height="12" viewBox="0 0 17 12"><rect x="0.75" y="0.75" width="15.5" height="10.5" rx="1" fill="none" stroke="#fff" stroke-width="1.5"/><path d="M1 1.2 8.5 7 16 1.2" fill="none" stroke="#fff" stroke-width="1.5"/></svg>
      </span>
      <span class="contact__icon" aria-label="Website">
        <svg width="16" height="16" viewBox="0 0 16 16" fill="none" stroke="#fff" stroke-width="1.3"><circle cx="8" cy="8" r="6.8"/><ellipse cx="8" cy="8" rx="3" ry="6.8"/><path d="M1.2 8h13.6M2.3 4.5h11.4M2.3 11.5h11.4"/></svg>
      </span>
      <span class="contact__icon" aria-label="Phone">
        <svg width="11" height="17" viewBox="0 0 11 17"><rect x="0.75" y="0.75" width="9.5" height="15.5" rx="1.6" fill="none" stroke="#fff" stroke-width="1.5"/><circle cx="5.5" cy="13.4" r="0.9" fill="#fff"/></svg>
      </span>
    </div>
    <ul class="contact__lines">
      <li>martin@brimoutreachpartners.com</li>
      <li>brimoutreachpartners.com</li>
      <li>+945 555 0142</li>
    </ul>
  </div>
</section>

</body>
</html>
```